Corporate Wall Mural for Office

We have several offices across North America and we want to have a corporate wall mural in each office, so we require a mural wall design that can be adjusted for different wall dimensions and still look good.

The first mural will be 239.5" x 112.5" it will be in our Toronto office - so the background city will be the Toronto skyline

I have attached a draft design and the content PNG file.

We want a different design that keeps the content outlined in the Mural Design Content PNG file.

Our corporate font is Gilroy Semi Bold

Our corporate colors are
Blue
C94
M70
Y0
K12
Pantone 2945C

Purple
C 80
M 78
PMS 2368 C

Sky Blue
C68
M34
PMS 2727 C
Our website is qorbelta.com

Founded in 2012, QBL is a leading provider of technology infrastructure solutions, specializing in Broadband, DAS/Private Networks, Fixed Wireless Access, Site Solutions, Carrier Networks, and Test & Measurement. Our mission is to empower organizations of all sizes with innovative connectivity and telecom infrastructure solutions to build the future of communications.

Target Market(s)

Target is the staff and visitors of our office

Industry/Entity Type

network infrastructure: both wireless and wireline

Font styles to use
Sans Serif
Other font styles liked:
• Gilroy Semi-Bold and Bold

Colors
0054AA
0677BA
7BADD7
CADEEF
E8F1F8

Requirements
Must have
• the info listed in the Mural Content.png file, our corporate colors. It should be bright and energetic.
Nice to have
• I like concept of the city silhouette from the draft design

```html
<!DOCTYPE html>
<html lang="en">
<head>
<meta charset="utf-8">
<title>QBL Office Mural</title>
<link href="https://fonts.googleapis.com/css2?family=Outfit:wght@400;500;600;700&display=swap" rel="stylesheet">
<style>
  :root {
    --navy: #0b1838;
    --panel-blue: #0a56a8;
    --brand-blue: #0054AA;
    --bright-blue: #1f7bff;
    --sky: #7BADD7;
    --pale: #E8F1F8;
    --white: #ffffff;
  }
  * { margin: 0; padding: 0; box-sizing: border-box; }
  html, body { width: 1200px; height: 564px; overflow: hidden; }
  body {
    position: relative;
    background: var(--navy);
    font-family: "Outfit", sans-serif;
    color: var(--white);
  }
  .skyline {
    position: absolute; left: 200px; top: 300px; width: 1000px; height: 264px;
    background:
      radial-gradient(ellipse 180px 60px at 620px 170px, rgba(90,150,255,.55), transparent 70%),
      linear-gradient(180deg, rgba(20,35,80,0) 0%, #1b2a5a 35%, #3a3d6e 55%, #7a5a55 68%, #1a2750 82%, #0a1430 100%);
  }
  .backdrop { position: absolute; inset: 0; }
  .brand-name {
    position: absolute; left: 46px; top: 44px;
    font-size: 54px; font-weight: 600; line-height: 1; letter-spacing: 1px;
  }
  .section-title { position: absolute; left: 49px; font-size: 21.3px; font-weight: 600; line-height: 1; }
  .unique-title { top: 133px; }
  .values-title { top: 310px; }
  .unique-row {
    position: absolute; left: 0; display: flex; align-items: flex-start;
    font-size: 13px; font-weight: 500; line-height: 15px;
  }
  .tag {
    background: var(--white); color: var(--brand-blue); font-weight: 600;
    width: 77px; height: 16px; text-align: right; padding-right: 2px; margin-right: 3px;
  }
  .custom-row {
    position: absolute; left: 0; top: 270px; width: 295px; height: 17px;
    background: var(--white); color: var(--brand-blue);
    font-size: 13px; font-weight: 600; padding-left: 49px; line-height: 17px;
  }
  .value { position: absolute; width: 80px; text-align: center; font-size: 10.6px; line-height: 12px; }
  .value-photo {
    width: 55px; height: 55px; border-radius: 50%; margin: 0 auto 6px;
    border: 1.5px solid var(--white);
    background: radial-gradient(circle at 40% 35%, #e9c9a8, #7f6a7a 60%, #3a4a70);
  }
  .headline-frame { position: absolute; left: 454px; top: 31px; }
  .headline {
    position: absolute; left: 455px; top: 50px; width: 705px; text-align: center;
    font-size: 26px; font-weight: 600; letter-spacing: .2px;
  }
  .subline {
    position: absolute; left: 430px; top: 113px; width: 712px; text-align: center;
    font-size: 21.5px; font-weight: 500;
  }
  .card {
    position: absolute; top: 176px; width: 198px; height: 249px;
    border: 2px solid var(--bright-blue); border-radius: 8px;
    background: rgba(8,16,42,.72);
  }
  .card-head {
    margin: 26px 18px 0; height: 24px; border-radius: 3px;
    background: var(--bright-blue); text-align: center;
    font-size: 14px; font-weight: 500; line-height: 24px;
  }
  .card-list { list-style: none; margin: 12px 0 0 20px; font-size: 11.5px; font-weight: 500; }
  .card-list li { position: relative; padding-left: 20px; line-height: 13.8px; margin-bottom: 5px; }
  .card-list li::before {
    content: ""; position: absolute; left: 1px; top: 4px; width: 6px; height: 6px;
    background: var(--white);
  }
  .card-list li.wrap-only { margin-top: -5px; }
  .card-list li.wrap-only::before { display: none; }
</style>
</head>
<body>
  <div class="skyline" role="img" aria-label="Night city skyline with a tall tower and a domed stadium reflected on the water"></div>

  <svg class="backdrop" width="1200" height="564" viewBox="0 0 1200 564" aria-hidden="true">
    <defs>
      <linearGradient id="panelFade" x1="0" y1="0" x2="1" y2="0">
        <stop offset="0" stop-color="#0a56a8"/>
        <stop offset="1" stop-color="#0d4fa0"/>
      </linearGradient>
    </defs>
    <polygon points="0,0 320,0 380,140 285,330 210,564 0,564" fill="url(#panelFade)"/>
    <polygon points="320,0 405,0 380,140" fill="#3c4aa8" opacity=".8"/>
    <polygon points="430,0 455,0 300,564 280,564" fill="#1f7bff" opacity=".85"/>
    <polygon points="1200,90 1200,230 1120,564 1080,564" fill="#1f7bff" opacity=".55"/>
    <polygon points="1070,380 1200,564 1130,564 1040,430" fill="#1f7bff" opacity=".6"/>
  </svg>

  <div class="brand-name">QBL</div>

  <h2 class="section-title unique-title">What Makes Us Unique?</h2>
  <div class="unique-row" style="top:170px"><span class="tag">QBL</span><span>Touch: We are more than a catalog</span></div>
  <div class="unique-row" style="top:201px"><span class="tag">QBL</span><span>Experience: A pleasure to do business with.<br>Proactive, Professional and Precise</span></div>
  <div class="unique-row" style="top:241px"><span class="tag">QBL</span><span>Solution: Design, Develop, and Deliver</span></div>
  <div class="custom-row">Custom Solutions: On-Time and On-Spec</div>

  <h2 class="section-title values-title">Our Core Values</h2>
  <div class="value" style="left:36px;top:351px"><div class="value-photo" role="img" aria-label="Two colleagues sharing a tablet"></div>People<br>First</div>
  <div class="value" style="left:102px;top:351px"><div class="value-photo" role="img" aria-label="Student thinking at a desk"></div>Intellectual<br>Curiosity</div>
  <div class="value" style="left:169px;top:351px"><div class="value-photo" role="img" aria-label="Hand stacking wooden blocks into steps"></div>Continuous<br>Improvement</div>
  <div class="value" style="left:36px;top:449px"><div class="value-photo" role="img" aria-label="Business handshake"></div>Customer<br>Focus</div>
  <div class="value" style="left:102px;top:449px"><div class="value-photo" role="img" aria-label="Hand making an OK gesture"></div>Results<br>Matter</div>

  <svg class="headline-frame" width="710" height="78" viewBox="0 0 710 78" aria-hidden="true">
    <polygon points="27,2 706,2 678,75 2,75" fill="none" stroke="#1f7bff" stroke-width="2.5"/>
  </svg>
  <h1 class="headline">ENABLING SOLUTIONS FOR A CONNECTED WORLD</h1>
  <p class="subline">We Distribute Products and Solution Services for Digital Infrastructure</p>

  <section class="card" style="left:418px">
    <h3 class="card-head">Our Capabilities</h3>
    <ul class="card-list">
      <li>Wireless Infrastructure</li>
      <li>Broadband &amp; Fiber</li>
      <li>Site Solutions</li>
      <li>Fixed Wireless Access</li>
      <li>Test &amp; Measurement</li>
      <li>DAS &amp; PWN</li>
      <li>Power Solutions</li>
    </ul>
  </section>

  <section class="card" style="left:628px">
    <h3 class="card-head">Solutions Services</h3>
    <ul class="card-list">
      <li>Kitting &amp; Logistics</li>
      <li>Professional Engineering</li>
      <li>Placeholder</li>
      <li>Placeholder</li>
      <li>Placeholder</li>
    </ul>
  </section>

  <section class="card" style="left:838px">
    <h3 class="card-head">Our Markets</h3>
    <ul class="card-list">
      <li>Carriers &amp; Cable<br>Companies</li>
      <li>Data Centers</li>
      <li>Utilities</li>
      <li>Federal Government</li>
      <li>Education</li>
      <li>Industrial Manufacturing</li>
      <li class="wrap-only">&amp; Digital Supply Chain</li>
    </ul>
  </section>
</body>
</html>
```